依頼詳細
このたびは、「緑茶ハイ・緑茶」専用メニュー表(A4片面)のデザインを募集いたします。

【メニュー表に入れていただきたい要素】
・ロゴ「凪色 Harbor」を、おしゃれなレトロ調で作成。メニュー表の上端にロゴを入れる。
・ユーモアで面白さもありつつ、少し高級感もあるデザイン。
・シリーズ化できる(これから緑茶以外にも紅茶ハイなども展開する可能性があります)
・「飲むならこの緑茶ハイがいいな!」と思われるようなデザインやキャッチコピー。
・飲食店の他メニュー表と一緒に置いていて、目を引くデザイン。

【コンペの流れ】
①ご応募ください。
②作成したデザインをご提出ください。
③コンペ終了後、採用者の選定をさせていただきます。

【デザイン提出方法】
PDFデータまたは、AIデータをお送りください。
※採用させていただいた場合、最終納品はイラストレーター形式(.ai)にてお願いします。

【備考】
ご提案いただいたデザインの編集依頼をすることがございます。
納期まで余裕をもってご提案頂けますと幸いです。
納期を過ぎてのご提案は受け付けておりませんので、予めご了承ください。
注意点】
コンペで採用となった場合、著作権は弊社に帰属します。

【継続依頼について】
スキル、センス、クオリティの高さなどにより、継続的な依頼を検討いたします。
記載項目
【メニュー表に入れていただきたい内容】
・緑茶ハイと緑茶の写真画像(デザイナー様の選定でお願いします)
・「緑茶ハイと緑茶」の値段が入れられる場所
(金額は仮で¥500と記載をお願いします)
・とっても美味しい静岡県産掛川市の茶葉を使用。
・無添加、無農薬のお茶粉。
・お茶粉のスティック写真を盛り込む(添付画像データをお使いください)。
※商品チラシデータを添付しています。
栄養や安全性、美味しさの詳細が書かれていますのでご覧ください。
サイズ
A4
ページ数
片面
希望イメージ
シンプル 複雑
単色 カラフル
暗い 明るい
日常 高級
遊び心 厳粛
未来的 伝統的
女性的 男性的
希望する色
緑系
納品ファイル
• イラストレーター形式 (.ai)
〆切を4/5に延長させていただきました!
どうか、デザイナーの方々のお力を貸してください!
よろしくお願いいたします。
みなさまのご協力をお待ちしております。
よろしくお願いいたします!
■ 選んだ理由

弊社のイメージするデザインに1番近かったため。

■ 提案者全員のお礼・コメント

素敵なデザインを作成していただき、ありがとうございます!

```html
<!DOCTYPE html>
<html lang="ja">
<head>
<meta charset="utf-8">
<title>緑茶ハイ・緑茶 メニュー</title>
<link rel="stylesheet" href="https://fonts.googleapis.com/css2?family=Shippori+Mincho:wght@500;700;800&family=Cormorant+Garamond:wght@500;600&display=swap">
<style>
  :root {
    --leaf: #4c8a3c;
    --leaf-deep: #3d7531;
    --lime: #d9ec8c;
    --lime-soft: #b7d96a;
    --cream: #f6f3c8;
    --white: #ffffff;
    --ink-green: #3f7a34;
    --tea: #3f8a2a;
  }
  * { margin: 0; padding: 0; box-sizing: border-box; }
  html, body { width: 855px; height: 1200px; overflow: hidden; }
  body {
    background: var(--leaf);
    font-family: "Shippori Mincho", serif;
    color: var(--white);
  }
  .menu {
    position: relative;
    width: 855px;
    height: 1200px;
    background: linear-gradient(180deg, var(--leaf) 0%, var(--leaf-deep) 100%);
    overflow: hidden;
  }
  .glow {
    position: absolute;
    left: 262px; top: 140px;
    width: 360px; height: 800px;
    border-radius: 48% 52% 46% 54% / 30% 34% 66% 70%;
    background: radial-gradient(ellipse at 50% 45%, var(--cream) 0%, var(--lime) 55%, var(--lime-soft) 100%);
    opacity: .95;
  }
  .drink-photo {
    position: absolute;
    left: 358px; top: 212px;
    width: 168px; height: 672px;
    clip-path: polygon(0 0, 100% 0, 88% 100%, 12% 100%);
    background: linear-gradient(180deg, #6fae4a 0%, var(--tea) 35%, #2e6e20 100%);
  }
  .brand-mark {
    position: absolute;
    left: 676px; top: 22px;
    width: 176px; height: 176px;
    border-radius: 50%;
    background: var(--white);
    border: 6px solid var(--leaf);
    outline: 2px solid var(--white);
    display: flex; align-items: center; justify-content: center;
    text-align: center;
  }
  .brand-name {
    color: var(--ink-green);
    font-weight: 800;
    font-size: 30px;
    line-height: 1.2;
  }
  .vertical { position: absolute; writing-mode: vertical-rl; white-space: nowrap; }
  .claim-main {
    left: 150px; top: 205px;
    font-size: 36px; font-weight: 700; letter-spacing: .06em;
  }
  .claim-main .circled {
    display: inline-block;
    width: 38px; height: 38px; line-height: 34px;
    border: 2px solid var(--white); border-radius: 50%;
    font-size: 26px; text-align: center;
    margin: 4px 0;
  }
  .claim-origin {
    left: 100px; top: 232px;
    font-size: 36px; font-weight: 700; letter-spacing: .06em;
  }
  .sub-title {
    left: 632px; top: 208px;
    font-size: 30px; font-weight: 700; letter-spacing: .04em;
  }
  .title {
    left: 700px; top: 262px;
    font-size: 60px; font-weight: 800; letter-spacing: .03em;
    line-height: 1;
  }
  .price {
    position: absolute;
    left: 738px; top: 738px;
    width: 92px; height: 92px;
    border-radius: 50%;
    background: var(--white);
    color: var(--ink-green);
    text-align: center;
    padding-top: 20px;
    line-height: 1;
  }
  .price-amount { font-family: "Cormorant Garamond", serif; font-weight: 600; font-size: 32px; }
  .price-unit { font-size: 12px; }
  .price-each { display: block; font-family: "Shippori Mincho", serif; font-size: 13px; margin-top: 4px; }
  .catch {
    position: absolute;
    left: 0; right: 0; top: 930px;
    text-align: center;
    font-size: 40px; font-weight: 700; letter-spacing: .04em;
  }
  .stick-photo {
    position: absolute;
    left: 612px; top: 996px;
    width: 16px; height: 72px;
    border-radius: 3px;
    background: linear-gradient(180deg, #e7c06a, #c8543a 55%, #7fb04a);
    transform: rotate(20deg);
  }
  .details {
    position: absolute;
    left: 0; right: 0; top: 1010px;
    text-align: center;
    font-size: 15px; font-weight: 500; line-height: 1.75;
    letter-spacing: .04em;
  }
  .footer-band {
    position: absolute;
    left: 0; right: 0; bottom: 0;
    height: 104px;
    background: linear-gradient(90deg, var(--lime-soft) 0%, var(--cream) 55%, var(--lime) 100%);
    display: flex; align-items: center; justify-content: center;
  }
  .footer-band::before {
    content: ""; position: absolute; left: 22px; right: 22px; top: 10px; bottom: 10px;
    border: 1.5px solid var(--ink-green);
  }
  .series-name {
    font-family: "Cormorant Garamond", serif;
    font-weight: 600; font-size: 46px; letter-spacing: .22em;
    color: var(--ink-green);
  }
</style>
</head>
<body>
  <main class="menu">
    <div class="glow"></div>
    <div class="drink-photo" role="img" aria-label="緑茶ハイのグラス写真"></div>

    <div class="brand-mark"><span class="brand-name">凪色<br>Harbor</span></div>

    <p class="vertical claim-main">カテキン含有量<span class="circled">多</span>とっても美味しい</p>
    <p class="vertical claim-origin">静岡県産掛川市の茶葉で緑茶ハイを。</p>

    <p class="vertical sub-title">無添加、無農薬のお茶粉の</p>
    <h1 class="vertical title">緑茶ハイ・緑茶</h1>

    <div class="price"><span class="price-amount">500</span><span class="price-unit">円</span><span class="price-each">each</span></div>

    <p class="catch">お茶の葉を、丸ごと粉末に。</p>
    <div class="stick-photo" role="img" aria-label="お茶粉スティックの写真"></div>
    <p class="details">農薬をお茶の栄養を逃すことなく、<br>食物繊維、ビタミンCなど30種の栄養素入り<br>100%植物由来、栄養素は青汁の5倍</p>

    <footer class="footer-band"><span class="series-name">RYOKUCHA</span></footer>
  </main>
</body>
</html>
```